Luxury Wine Label for New Startup Winery

We need a wine label for our new winery startup. We have worked with a local designer but do not feel the resulting label / logo have the elevation required to present our brand as a luxury wine. Our winery is called "Harrowgate Vineyards" and we are focused on extremely high quality hand crafted artisan and estate wines from the Pacific Northwest.
We would like to see designs that utilize a tree line, or other imagery that represents the "Harrowgate" part of our company name. Another interesting feature could be wood grain.
A logo will be required based on your design so please design with this in mind:
This logo should be consistent with the wine bottle label design, and should be representative of our high end exclusive wine while giving a sense of place (Oregon/ Pacific Northwest.)
I will supply an image of the design we received from our local designer, PLEASE NOTE: in general we do like wood grain and tree line concepts but feel the execution was poorly done.
ATTN: Logo design should be suitable for use on: Bottles (Red wine/rose/white wine), Bussiness cards, vehicle signage, business signage, etc
P.S.:
If you have a design that is not outside the box we are still interested in seeing it.
Label is for a burgundy style bottle with a label height of 3.5 - 4" and a width of 3.5-4"
any label <= 4"x4" and >=3.5"x3.5" will be acceptable:
HOWEVER Width should be greater than or equal to height due to the bottle format
Target Market(s)
Wine enthusiasts with adequate discretionary budgets to afford $100 bottles of wine.
Industry/Entity Type
Wine / Winery
Requirements
Must have
- A sense of luxury, a feel of exclusivity, and a theme consistent with our product and brand name
Nice to have
- Tree line, wood grain or other wood themes. Serif fonts
Should not have
- anything cheesy, off topic, hard to read script fonts or anything that makes the label hard to read from a few feet away or too busy

```html
<!DOCTYPE html>
<html lang="en">
<head>
<meta charset="utf-8">
<title>Harrowgate Vineyards — Rosé Label</title>
<link href="https://fonts.googleapis.com/css2?family=Poiret+One&family=Allura&display=swap" rel="stylesheet">
<style>
  :root {
    --backdrop: #e6e6e6;
    --label-red: #a5181e;
    --label-red-light: #b3222a;
    --gold: #e9b934;
    --gold-deep: #c8901a;
    --gold-bright: #f6d45a;
    --badge-white: #ffffff;
    --rose-tint: #c9565b;
  }
  * { box-sizing: border-box; margin: 0; padding: 0; }
  html, body {
    width: 1200px;
    height: 1000px;
    overflow: hidden;
    background: var(--backdrop);
  }
  .canvas {
    position: relative;
    width: 1200px;
    height: 1000px;
  }
  .wine-label {
    position: absolute;
    left: 200px;
    top: 100px;
    width: 800px;
    height: 800px;
    background: radial-gradient(ellipse at 50% 55%, var(--label-red-light) 0%, var(--label-red) 75%);
  }
  .label-frame {
    position: absolute;
    inset: 20px;
    border: 2px solid var(--gold);
  }
  .treeline-art {
    position: absolute;
    left: 148px;
    top: 68px;
    width: 507px;
    height: 184px;
    border-radius: 90px 90px 6px 6px;
    background: linear-gradient(180deg, var(--gold-bright) 0%, var(--gold) 55%, var(--gold-deep) 100%);
    opacity: 0.9;
  }
  .winery-name {
    position: absolute;
    left: 0;
    right: 0;
    text-align: center;
    color: var(--gold);
    font-family: "Poiret One", sans-serif;
    text-transform: uppercase;
    line-height: 1;
  }
  .winery-name--estate {
    top: 292px;
    font-size: 54px;
    letter-spacing: 1px;
  }
  .winery-name--vineyards {
    top: 348px;
    font-size: 80px;
    letter-spacing: 1px;
  }
  .wine-variety {
    position: absolute;
    left: 0;
    right: 0;
    top: 488px;
    text-align: center;
    color: var(--gold);
    font-family: "Allura", cursive;
    font-size: 100px;
    line-height: 1;
  }
  .variety-badge {
    position: absolute;
    left: 340px;
    top: 615px;
    width: 120px;
    height: 120px;
    border-radius: 50%;
    background: var(--badge-white);
  }
  .variety-badge__art {
    position: absolute;
    left: 30px;
    top: 30px;
    width: 60px;
    height: 60px;
    border-radius: 50%;
    background: radial-gradient(circle, var(--rose-tint) 0%, rgba(201, 86, 91, 0.35) 100%);
  }
</style>
</head>
<body>
  <main class="canvas">
    <section class="wine-label">
      <div class="label-frame"></div>
      <div class="treeline-art" role="img" aria-label="Gold illustration of a stand of fir trees on a hill between mountain peaks, with birds in flight"></div>
      <h1 class="winery-name winery-name--estate">Harrowgate</h1>
      <p class="winery-name winery-name--vineyards">Vineyards</p>
      <p class="wine-variety">Rose</p>
      <div class="variety-badge">
        <div class="variety-badge__art" role="img" aria-label="Red line illustration of a rose blossom"></div>
      </div>
    </section>
  </main>
</body>
</html>
```